Young, dynamic furniture company requires leaflet design

We require a new leaflet for our modern furniture company which supplies furniture and appliances to the property and development market.
Bramblecourt Furniture has become one of the leading furniture & appliance suppliers to the property market withing London. With over 10 years experience, we have increased our business to supply not only Private Landlords and Managing Agents, but also Property Developers, Housing Associations and Local Councils.
We offer not only a complete range of furniture which includes beds, wardrobes, dining sets and sofas, but also a high quality, full delivery and assembly service to help you with all our furnishing needs.

Target Market(s)

Private Landlords, Developers, Letting & Managing Agents

Industry/Entity Type

Furniture Store

Font styles to use
Sans Serif

Colors
0255a3
3176b5
85abd2
cfdeed
eaf1f7

Requirements
Must have
• Contact details,
• Our services:
• FREE next day delivery within the M25
• Free furniture assembly
• Free key pick up & drop off
• Free furniture removal (on a like-for-like basis)
• All types of furniture supplied - from basic to luxury

```html
<!DOCTYPE html>
<html lang="en">
<head>
<meta charset="utf-8">
<title>Bramblecourt Furniture – Leaflet</title>
<link href="https://fonts.googleapis.com/css2?family=Lato:wght@400;700;900&display=swap" rel="stylesheet">
<style>
  :root {
    --blue-deep: #0255a3;
    --blue-mid: #3176b5;
    --blue-soft: #85abd2;
    --blue-pale: #cfdeed;
    --blue-mist: #eaf1f7;
    --ink: #3a3f47;
    --ink-soft: #5c636d;
    --paper: #ffffff;
    --backdrop: #d9dbde;
  }
  * { box-sizing: border-box; margin: 0; padding: 0; }
  html, body { width: 1200px; height: 1200px; overflow: hidden; }
  body {
    background: var(--backdrop);
    font-family: "Lato", Arial, sans-serif;
    color: var(--ink);
    position: relative;
  }
  .leaflet {
    position: absolute; left: 204px; top: 40px;
    width: 792px; height: 1120px;
    background: var(--paper);
    overflow: hidden;
  }
  .call-line {
    position: absolute; left: 40px; top: 40px;
    font-size: 26px; font-weight: 900; color: var(--blue-deep);
    letter-spacing: 0.5px;
  }
  .brand {
    position: absolute; right: 30px; top: 18px;
    text-align: center; width: 290px;
  }
  .brand-mark {
    width: 46px; height: 46px; margin: 0 auto 8px;
    background: var(--blue-deep);
  }
  .brand-name {
    font-size: 18px; font-weight: 700; color: var(--blue-deep);
    letter-spacing: 0.5px; white-space: nowrap;
  }
  .brand-tagline {
    font-size: 10px; font-weight: 700; color: var(--blue-deep);
    letter-spacing: 1.4px; margin-top: 3px; white-space: nowrap;
  }

  .hero-photo {
    position: absolute; left: 0; top: 135px; width: 792px; height: 370px;
    background: linear-gradient(135deg, #e9dcc2 0%, #d8c4a0 40%, #b08a5e 75%, #7a5a3a 100%);
  }

  .experience-band {
    position: absolute; left: 0; top: 505px; width: 792px; height: 130px;
    background: var(--blue-mist);
  }
  .experience-title {
    position: absolute; left: 40px; top: 18px;
    font-size: 58px; font-weight: 900; color: var(--blue-deep); line-height: 1;
  }
  .experience-sub {
    position: absolute; left: 40px; top: 80px;
    font-size: 26px; font-weight: 400; color: var(--blue-deep); letter-spacing: 0.5px;
  }
  .room-thumbs { position: absolute; right: 30px; top: 14px; display: flex; gap: 14px; }
  .room-thumb {
    width: 104px; height: 104px; border-radius: 50%;
    border: 5px solid var(--blue-mid);
  }
  .thumb-bed { background: linear-gradient(160deg, #f0ece4, #c9b79a); }
  .thumb-bedroom { background: linear-gradient(160deg, #dfe3e8, #8c96a3); }
  .thumb-chairs { background: linear-gradient(160deg, #efe6d8, #6b4a2e); }

  .about { position: absolute; left: 40px; top: 655px; width: 712px; }
  .section-heading { font-size: 22px; font-weight: 700; color: var(--blue-deep); margin-bottom: 10px; }
  .about-columns { display: flex; gap: 30px; }
  .about-columns p { flex: 1; font-size: 12.5px; line-height: 1.45; color: var(--ink-soft); }

  .offer { position: absolute; left: 40px; top: 775px; width: 330px; }
  .offer-heading { font-size: 24px; font-weight: 700; color: var(--blue-deep); line-height: 1.15; margin-bottom: 14px; }
  .tick-list { list-style: none; }
  .tick-list li {
    position: relative; padding-left: 18px; margin-bottom: 7px;
    font-size: 13px; line-height: 1.35; color: var(--ink-soft);
  }
  .tick-list li::before {
    content: ""; position: absolute; left: 0; top: 5px;
    width: 8px; height: 8px; background: var(--blue-deep);
  }
  .divider {
    position: absolute; left: 396px; top: 790px; width: 2px; height: 170px;
    background: var(--blue-pale);
  }
  .services { position: absolute; left: 430px; top: 790px; width: 340px; }
  .services .offer-heading { margin-bottom: 12px; }

  .contact { position: absolute; left: 40px; top: 990px; width: 420px; }
  .phones { display: flex; gap: 34px; margin-bottom: 14px; }
  .phone { display: flex; align-items: center; gap: 8px; font-size: 18px; font-weight: 700; color: var(--blue-deep); }
  .phone svg { width: 18px; height: 18px; }
  .contact-line { display: flex; align-items: center; gap: 8px; font-size: 12px; color: var(--ink-soft); margin-bottom: 7px; }
  .contact-line svg { width: 14px; height: 14px; flex: none; }

  .furniture-photo {
    position: absolute; left: 490px; top: 984px; width: 272px; height: 110px;
    background: linear-gradient(90deg, #c89a5e 0%, #a87940 45%, #2a1f1a 60%, #1a1411 100%);
  }
  .footer-bar {
    position: absolute; left: 0; bottom: 0; width: 792px; height: 26px;
    background: var(--blue-deep);
  }
</style>
</head>
<body>
  <main class="leaflet">
    <header>
      <div class="call-line">CALL US NOW 020 7946 0321</div>
      <div class="brand">
        <div class="brand-mark"></div>
        <div class="brand-name">BRAMBLECOURT FURNITURE</div>
        <div class="brand-tagline">TRADE FURNITURE SOLUTIONS</div>
      </div>
    </header>

    <div class="hero-photo" role="img" aria-label="Bright furnished living room with a sofa, coffee table, lamp and staircase"></div>

    <section class="experience-band">
      <div class="experience-title">WITH OVER</div>
      <div class="experience-sub">10 YEARS EXPERIENCE</div>
      <div class="room-thumbs">
        <div class="room-thumb thumb-bed" role="img" aria-label="Made-up bed"></div>
        <div class="room-thumb thumb-bedroom" role="img" aria-label="Furnished bedroom"></div>
        <div class="room-thumb thumb-chairs" role="img" aria-label="Modern dining chairs"></div>
      </div>
    </section>

    <section class="about">
      <h2 class="section-heading">About us</h2>
      <div class="about-columns">
        <p>Bramblecourt Furniture has become one of the leading furniture &amp; appliance suppliers to the property market withing London. With over 10 years experience,</p>
        <p>we have increased our business to supply not only Private Landlords and Managing Agents, but also Property Developers, Housing Associations and Local Councils.</p>
      </div>
    </section>

    <section class="offer">
      <h2 class="offer-heading">We offer not only<br>a complete range of</h2>
      <ul class="tick-list">
        <li>Furniture which includes beds</li>
        <li>Wardrobes</li>
        <li>Dining sets and sofas<br>but also a high quality</li>
        <li>Full delivery and assembly service to help<br>you with all our furnishing needs.</li>
      </ul>
    </section>

    <div class="divider"></div>

    <section class="services">
      <h2 class="offer-heading">Our services:</h2>
      <ul class="tick-list">
        <li>FREE next day delivery within the M25</li>
        <li>Free furniture assembly</li>
        <li>Free key pick up &amp; drop off</li>
        <li>Free furniture removal (on a like-for-like basis)</li>
        <li>All types of furniture supplied - from basic to luxury</li>
      </ul>
    </section>

    <section class="contact">
      <div class="phones">
        <div class="phone">
          <svg viewBox="0 0 24 24"><path fill="#0255a3" d="M6.6 10.8c1.4 2.8 3.8 5.1 6.6 6.6l2.2-2.2c.3-.3.7-.4 1-.2 1.1.4 2.3.6 3.6.6.6 0 1 .4 1 1V20c0 .6-.4 1-1 1C10.6 21 3 13.4 3 4c0-.6.4-1 1-1h3.5c.6 0 1 .4 1 1 0 1.3.2 2.5.6 3.6.1.3 0 .7-.2 1z"/></svg>
          020 7946 0321
        </div>
        <div class="phone">
          <svg viewBox="0 0 24 24"><rect x="3" y="6" width="18" height="12" rx="2" fill="#0255a3"/><rect x="6" y="3" width="12" height="4" fill="#0255a3"/><rect x="7" y="14" width="10" height="7" fill="#fff" stroke="#0255a3" stroke-width="1.5"/></svg>
          020 7946 0388
        </div>
      </div>
      <div class="contact-line">
        <svg viewBox="0 0 24 24"><path fill="#0255a3" d="M12 2C8.1 2 5 5.1 5 9c0 5.2 7 13 7 13s7-7.8 7-13c0-3.9-3.1-7-7-7zm0 9.5a2.5 2.5 0 1 1 0-5 2.5 2.5 0 0 1 0 5z"/></svg>
        12B Hollin Trade Park, Fernmoor, London N9 4QT
      </div>
      <div class="contact-line">
        <svg viewBox="0 0 24 24"><circle cx="12" cy="12" r="9" fill="none" stroke="#0255a3" stroke-width="2"/><path d="M3 12h18M12 3c3 3 3 15 0 18M12 3c-3 3-3 15 0 18" fill="none" stroke="#0255a3" stroke-width="1.5"/></svg>
        trade-bramblecourt.co.uk
      </div>
    </section>

    <div class="furniture-photo" role="img" aria-label="Wooden dining table with dark leather dining chairs"></div>

    <div class="footer-bar"></div>
  </main>
</body>
</html>
```